2018 PVLTA Conference Theme Artwork

We need artwork designed around the theme of this year's human resources conference. The theme is "Celebrating 20 Years Together Towards Tomorrow". The artwork should be designed as a 4x6 postcard and will eventually be adapted/reformatted to use on the registration website, sales materials, e-newsletters, conference guide cover and signage.

Target Market(s)

Attendees are human resources professionals. Exhibitors and sponsors are companies who want to sell their products/services to human resource professionals

Colors

Designer to choose colors to be used in the design.

Requirements
Must have
• NO BORING PIXVAULT IMAGERY PLEASE.
• Theme: Celebrating 20 Years Together Towards Tomorrow
• Event: 20th Annual PVLT Conference
• Dates/Times: Tuesday, May 15, 2018, 12:30pm - 5:00pm and Wednesday, May 16, 2018 7:30am - 5:30pm
• Website: pvltsummit.example
• Location: The HALL at the Corvane Lindley
Nice to have
• Engaging, celebratory, visually attractive
Should not have
• NO BORING PIXVAULT IMAGERY.

```html
<!DOCTYPE html>
<html lang="en">
<head>
<meta charset="utf-8">
<title>2018 PVLTA Conference – Theme Artwork</title>
<link rel="stylesheet" href="https://fonts.googleapis.com/css2?family=Jost:ital,wght@0,400;0,500;0,600;0,800;1,400&display=swap">
<style>
  :root {
    --ink: #1f2d3a;
    --red: #b71f2d;
    --grey-text: #333333;
    --panel-top: #eef0f1;
    --panel-bottom: #ffffff;
    --page: #ffffff;
    --soft-line: #9aa4ad;
  }
  html, body {
    margin: 0;
    padding: 0;
    width: 1200px;
    height: 1200px;
    overflow: hidden;
    background: var(--page);
  }
  .board { display: block; width: 1200px; height: 1200px; }
  .board-title {
    font-family: "Jost", sans-serif;
    font-weight: 600; font-size: 46px; letter-spacing: 3px;
    fill: var(--grey-text);
  }
  .spec-note { font-family: "Jost", sans-serif; font-size: 22px; fill: var(--grey-text); }
  .kicker {
    font-family: "Jost", sans-serif; font-weight: 500; font-size: 52px;
    letter-spacing: 18px; fill: var(--ink);
  }
  .headline {
    font-family: "Jost", sans-serif; font-weight: 800; font-size: 150px;
  }
  .headline-red { fill: var(--red); }
  .headline-ink { fill: var(--ink); }
  .timeline-line { stroke: var(--soft-line); stroke-width: 3; }
  .timeline-dot { fill: var(--ink); }
  .timeline-dot-now { fill: var(--red); }
  .timeline-year {
    font-family: "Jost", sans-serif; font-weight: 500; font-size: 22px;
    letter-spacing: 2px; fill: var(--ink);
  }
  .event-name { font-family: "Jost", sans-serif; font-weight: 500; font-size: 42px; fill: var(--red); }
  .venue { font-family: "Jost", sans-serif; font-style: italic; font-size: 30px; fill: var(--ink); }
  .schedule { font-family: "Jost", sans-serif; font-size: 26px; fill: var(--ink); letter-spacing: 0.5px; }
  .divider { stroke: var(--red); stroke-width: 2.5; }
  .learn-more {
    font-family: "Jost", sans-serif; font-size: 26px; fill: var(--ink);
    text-anchor: end; letter-spacing: 0.5px;
  }
  .website {
    font-family: "Jost", sans-serif; font-weight: 500; font-size: 28px;
    fill: var(--red); text-anchor: end;
  }
</style>
</head>
<body>
<svg class="board" viewBox="0 0 1500 1500" xmlns="http://www.w3.org/2000/svg">
  <defs>
    <linearGradient id="panelTone" x1="0" y1="0" x2="1" y2="1">
      <stop offset="0" stop-color="#eef0f1"/>
      <stop offset="0.55" stop-color="#ffffff"/>
      <stop offset="1" stop-color="#eef0f1"/>
    </linearGradient>
  </defs>

  <text class="board-title" x="750" y="188" text-anchor="middle">2018 PVLTA CONFERENCE</text>

  <g class="postcard">
    <rect x="74" y="288" width="1352" height="900" fill="url(#panelTone)"/>

    <g class="theme">
      <text class="kicker" x="160" y="372">CELEBRATING</text>
      <text class="headline headline-red" x="160" y="560" textLength="1180" lengthAdjust="spacing">20 YEARS</text>
      <text class="headline headline-ink" x="160" y="720" textLength="1180" lengthAdjust="spacing">TOGETHER</text>

      <g class="timeline">
        <line class="timeline-line" x1="160" y1="790" x2="1340" y2="790"/>
        <circle class="timeline-dot" cx="160" cy="790" r="6"/>
        <circle class="timeline-dot" cx="219" cy="790" r="4"/>
        <circle class="timeline-dot" cx="278" cy="790" r="4"/>
        <circle class="timeline-dot" cx="337" cy="790" r="4"/>
        <circle class="timeline-dot" cx="396" cy="790" r="4"/>
        <circle class="timeline-dot" cx="455" cy="790" r="4"/>
        <circle class="timeline-dot" cx="514" cy="790" r="4"/>
        <circle class="timeline-dot" cx="573" cy="790" r="4"/>
        <circle class="timeline-dot" cx="632" cy="790" r="4"/>
        <circle class="timeline-dot" cx="691" cy="790" r="4"/>
        <circle class="timeline-dot" cx="750" cy="790" r="4"/>
        <circle class="timeline-dot" cx="809" cy="790" r="4"/>
        <circle class="timeline-dot" cx="868" cy="790" r="4"/>
        <circle class="timeline-dot" cx="927" cy="790" r="4"/>
        <circle class="timeline-dot" cx="986" cy="790" r="4"/>
        <circle class="timeline-dot" cx="1045" cy="790" r="4"/>
        <circle class="timeline-dot" cx="1104" cy="790" r="4"/>
        <circle class="timeline-dot" cx="1163" cy="790" r="4"/>
        <circle class="timeline-dot" cx="1222" cy="790" r="4"/>
        <circle class="timeline-dot" cx="1281" cy="790" r="4"/>
        <circle class="timeline-dot-now" cx="1340" cy="790" r="10"/>
        <text class="timeline-year" x="160" y="830">1998</text>
        <text class="timeline-year" x="1340" y="830" text-anchor="end">2018</text>
      </g>

      <text class="kicker" x="1340" y="900" text-anchor="end">TOWARDS TOMORROW</text>
    </g>

    <g class="event-details">
      <text class="event-name" x="156" y="993">20th Annual PVLT Conference</text>
      <text class="venue" x="156" y="1037">The HALL at the Corvane Lindley</text>
      <text class="schedule" x="156" y="1094">Tuesday, May 15, 2018</text>
      <text class="schedule" x="156" y="1131">12:30pm - 5:00pm</text>
      <line class="divider" x1="452" y1="1074" x2="452" y2="1146"/>
      <text class="schedule" x="481" y="1094">Wednesday, May 16, 2018</text>
      <text class="schedule" x="481" y="1131">7:30am - 5:30pm</text>
      <text class="learn-more" x="1338" y="1100">Learn more at</text>
      <text class="website" x="1344" y="1132">pvltsummit.example</text>
    </g>
  </g>

  <g class="spec-notes">
    <text class="spec-note" x="74" y="1249">SIZE: 4” x 6”</text>
    <text class="spec-note" x="74" y="1279">FILE TYPE: Flyer Design</text>
    <text class="spec-note" x="74" y="1309">FILE FORMAT: JPEG</text>
  </g>
</svg>
</body>
</html>
```